Business Card for Jewelry Business

We need a new namecard design for a jewelry company based in Bangkok, Thailand. We have a new website recently and want the new namecard to reflect our new modern image. I have uploaded our old namecard to show you the information that needs to be on the namecard. Pls check our website www.qelburn.com for the new color scheme to help design the new namecard.

```html
<!DOCTYPE html>
<html lang="en">
<head>
<meta charset="utf-8">
<title>Qelburn Manufacturers – Business Card</title>
<link rel="stylesheet" href="https://fonts.googleapis.com/css2?family=Open+Sans:wght@400;700&family=Crimson+Text:ital,wght@1,700&display=swap">
<style>
  :root {
    --stage: #2b2b2d;
    --card-dark: #231f20;
    --card-teal: #53c4c9;
    --ink-light: #ffffff;
    --ink-cream: #ece6dc;
    --shadow: rgba(0,0,0,0.55);
  }
  * { margin: 0; padding: 0; box-sizing: border-box; }
  html, body {
    width: 1200px; height: 1015px; overflow: hidden;
    background: var(--stage);
    font-family: "Open Sans", Arial, sans-serif;
  }
  .canvas { position: relative; width: 1200px; height: 1015px; }
  .card {
    position: absolute; width: 640px; height: 366px;
    box-shadow: 0 14px 30px var(--shadow);
    overflow: hidden;
  }
  .card--front { left: 120px; top: 100px; background: var(--card-dark); }
  .card--back  { left: 440px; top: 540px; background: var(--card-teal); color: var(--ink-light); }

  .brand {
    position: absolute; left: 0; right: 0; top: 128px;
    display: flex; align-items: center; justify-content: center; gap: 14px;
  }
  .brand__mark { width: 34px; height: 34px; border-radius: 50%; background: var(--card-teal); }
  .brand__name {
    font-weight: 400; font-size: 30px; letter-spacing: 3px;
    color: var(--ink-cream); text-transform: uppercase;
  }
  .socials {
    position: absolute; left: 0; right: 0; bottom: 46px;
    display: flex; justify-content: center; gap: 34px;
    color: var(--ink-light); font-size: 15px;
  }
  .social { display: flex; align-items: center; gap: 9px; }
  .social__dot { width: 18px; height: 18px; border-radius: 50%; background: #4a6fb5; }
  .social__dot--alt { background: #d9476b; }

  .details { position: absolute; left: 40px; top: 36px; }
  .person__name {
    font-family: "Crimson Text", Georgia, serif; font-style: italic; font-weight: 700;
    font-size: 26px; letter-spacing: 1px; line-height: 1;
  }
  .person__role { font-size: 14px; margin-top: 4px; }
  .company { margin-top: 16px; font-size: 13.5px; line-height: 1.32; }
  .company__name { font-weight: 700; font-size: 14.5px; }
  .contacts { list-style: none; margin-top: 16px; font-size: 13.5px; }
  .contacts li { display: flex; align-items: center; gap: 10px; line-height: 1.45; }
  .contacts svg { width: 15px; height: 15px; flex: none; }
</style>
</head>
<body>
<main class="canvas">
  <section class="card card--front" aria-label="Card front">
    <div class="brand">
      <span class="brand__mark"></span>
      <span class="brand__name">Qelburn Manufacturers</span>
    </div>
    <div class="socials">
      <span class="social"><span class="social__dot"></span>Qelburn Manufacturers</span>
      <span class="social"><span class="social__dot social__dot--alt"></span>@QelburnMfr</span>
    </div>
  </section>

  <section class="card card--back" aria-label="Card back">
    <div class="details">
      <p class="person__name">NARA PIMCHAI</p>
      <p class="person__role">Sales &amp; Product Development Manager</p>
      <p class="company">
        <span class="company__name">Qelburn Manufacturers Co.,Ltd.</span><br>
        218 Moo 7 Rama Phatthana Road,<br>
        Export Processing Zone 2,<br>
        Riverside Industrial Estate,<br>
        Bang Sao, Bangkok 10230 Thailand.
      </p>
      <ul class="contacts">
        <li><svg viewBox="0 0 16 16" fill="none" stroke="currentColor" stroke-width="1.6"><path d="M3 2h3l1 3-2 1a8 8 0 0 0 5 5l1-2 3 1v3a1 1 0 0 1-1 1A12 12 0 0 1 2 3a1 1 0 0 1 1-1z"/></svg>+662-555-0142-4</li>
        <li><svg viewBox="0 0 16 16" fill="currentColor"><rect x="4" y="1" width="8" height="4"/><rect x="1" y="6" width="14" height="6" rx="1"/><rect x="4" y="10" width="8" height="5" fill="var(--card-teal)" stroke="currentColor"/></svg>+662-555-0178</li>
        <li><svg viewBox="0 0 16 16" fill="none" stroke="currentColor" stroke-width="1.6"><rect x="1" y="3" width="14" height="10"/><path d="M1 3l7 6 7-6"/></svg>nara@qelburn.com</li>
        <li><svg viewBox="0 0 16 16" fill="none" stroke="currentColor" stroke-width="1.6"><rect x="1" y="3" width="14" height="10"/><path d="M1 3l7 6 7-6"/></svg>info@qelburn.com</li>
        <li><svg viewBox="0 0 16 16" fill="none" stroke="currentColor" stroke-width="1.3"><circle cx="8" cy="8" r="6.5"/><ellipse cx="8" cy="8" rx="3" ry="6.5"/><path d="M1.5 8h13M2.5 4.5h11M2.5 11.5h11"/></svg>http://www.qelburn.net</li>
      </ul>
    </div>
  </section>
</main>
</body>
</html>
```